Corporate consulting business needs a business card

I want a professional business card.... surprise me

Updates

Reason: i dont think 2 days is enough

Target Market(s)

Corprorate and Not for Profit firms and organisations

Industry/Entity Type

Consulting

Contact Information for Business Card

Logo
Corporate Consulting Services
Clear Advice, Sound Plans, Lasting Value
Tovan Presfield
Director
0427 31 94 62 (Larger)
tovan@tp-advisory.com.au
www.tp-advisory.com.au
include little icons beside the contact info:

- Envelope = email
- Phone = phone
- Globe = website

Font styles to use
Serif
Sans Serif

Requirements
Must have
• Professional and clean
Nice to have
• you tell me

```html
<!DOCTYPE html>
<html lang="en">
<head>
<meta charset="utf-8">
<title>TP Advisory – Business Card</title>
<link rel="stylesheet" href="https://fonts.googleapis.com/css2?family=Cinzel:wght@600&family=Montserrat:wght@400;500;600&display=swap">
<style>
  :root {
    --backdrop: #2f2f31;
    --card: #060606;
    --ink: #ffffff;
    --ink-soft: #d9d9d9;
    --accent: #5a3a26;
    --band-light: #ffffff;
  }
  * { margin: 0; padding: 0; box-sizing: border-box; }
  html, body { width: 1200px; height: 900px; overflow: hidden; }
  body {
    background: var(--backdrop);
    position: relative;
    font-family: "Montserrat", Arial, sans-serif;
    color: var(--ink);
  }
  .card {
    position: absolute;
    width: 600px;
    height: 340px;
    background: var(--card);
    border-radius: 24px;
    overflow: hidden;
    box-shadow: 0 18px 40px rgba(0,0,0,.45);
  }

  /* Front */
  .card--front { left: 90px; top: 70px; }
  .brand {
    position: absolute;
    left: 0; right: 0; top: 100px;
    display: flex;
    align-items: center;
    justify-content: center;
    gap: 18px;
  }
  .brand__mark {
    width: 56px; height: 56px;
    border: 4px solid var(--ink);
    border-radius: 50%;
    flex: none;
  }
  .brand__name {
    font-family: "Cinzel", Georgia, serif;
    font-weight: 600;
    font-size: 34px;
    letter-spacing: 1px;
    color: var(--ink);
    white-space: nowrap;
  }
  .card--front .web {
    position: absolute;
    left: 0; right: 0; top: 250px;
    text-align: center;
    font-size: 15px;
    letter-spacing: .3px;
    color: var(--ink-soft);
  }

  /* Back */
  .card--back { left: 510px; top: 480px; }
  .card--back .brand {
    left: 28px; right: auto; top: 112px;
    width: 240px;
    gap: 10px;
  }
  .card--back .brand__mark { width: 36px; height: 36px; border-width: 3px; }
  .card--back .brand__name { font-size: 23px; letter-spacing: .5px; }
  .divider {
    position: absolute;
    left: 292px; top: 62px;
    width: 1px; height: 150px;
    background: linear-gradient(to bottom, transparent, #9a9a9a 30%, #9a9a9a 70%, transparent);
  }
  .contact {
    position: absolute;
    left: 318px; top: 56px;
  }
  .contact__name {
    font-weight: 600;
    font-size: 21px;
    letter-spacing: .3px;
  }
  .contact__role {
    font-size: 13px;
    color: var(--ink-soft);
    margin-top: 2px;
  }
  .contact__list { list-style: none; margin-top: 18px; }
  .contact__item {
    display: flex;
    align-items: center;
    gap: 10px;
    font-size: 13px;
    color: var(--ink-soft);
    margin-bottom: 7px;
  }
  .contact__item--phone { font-size: 15px; color: var(--ink); }
  .contact__item strong { font-weight: 600; color: var(--ink); }
  .icon { width: 12px; height: 12px; flex: none; }

  .band {
    position: absolute;
    left: 0; right: 0; bottom: 0;
    height: 30px;
    display: flex;
  }
  .band__light--left { width: 20%; background: var(--band-light); }
  .band__tagline {
    width: 56%;
    background: var(--accent);
    display: flex;
    align-items: center;
    justify-content: center;
    font-weight: 500;
    font-size: 12.5px;
    letter-spacing: .6px;
    text-transform: uppercase;
    white-space: nowrap;
  }
  .band__light--right { flex: 1; background: var(--band-light); }
</style>
</head>
<body>

  <section class="card card--front" aria-label="Business card front">
    <div class="brand">
      <span class="brand__mark"></span>
      <span class="brand__name">TP ADVISORY</span>
    </div>
    <p class="web">www.tp-advisory.com.au</p>
  </section>

  <section class="card card--back" aria-label="Business card back">
    <div class="brand">
      <span class="brand__mark"></span>
      <span class="brand__name">TP ADVISORY</span>
    </div>

    <div class="divider"></div>

    <div class="contact">
      <p class="contact__name">Tovan Presfield</p>
      <p class="contact__role">Director</p>
      <ul class="contact__list">
        <li class="contact__item contact__item--phone">
          <svg class="icon" viewBox="0 0 24 24" fill="#ffffff"><path d="M6.6 10.8a15.1 15.1 0 0 0 6.6 6.6l2.2-2.2c.3-.3.7-.4 1-.2 1.1.4 2.3.6 3.6.6.6 0 1 .4 1 1V20c0 .6-.4 1-1 1A17 17 0 0 1 3 4c0-.6.4-1 1-1h3.5c.6 0 1 .4 1 1 0 1.3.2 2.5.6 3.6.1.3 0 .7-.2 1z"/></svg>
          0427 31 94 62
        </li>
        <li class="contact__item">
          <svg class="icon" viewBox="0 0 24 24" fill="none" stroke="#ffffff" stroke-width="2"><rect x="3" y="5" width="18" height="14" rx="1"/><path d="M3 6l9 7 9-7"/></svg>
          tovan@tp-advisory.com.au
        </li>
        <li class="contact__item">
          <svg class="icon" viewBox="0 0 24 24" fill="none" stroke="#ffffff" stroke-width="2"><circle cx="12" cy="12" r="9"/><path d="M3 12h18M12 3c3 3 3 15 0 18M12 3c-3 3-3 15 0 18"/></svg>
          <span>www.<strong>tp-advisory</strong>.com.au</span>
        </li>
      </ul>
    </div>

    <div class="band">
      <span class="band__light--left"></span>
      <span class="band__tagline">Clear Advice, Sound Plans, Lasting Value</span>
      <span class="band__light--right"></span>
    </div>
  </section>

</body>
</html>
```